Using attached logo that has been created

Business card with logo that's attached. Maybe with water or the cartoon van in background. Looking for it to not be so plain and not too white.
Information to include;
Dario Whitlock
(555) 208-7713
Info@mossbrookpipeworks.example
www.mossbrookpipeworks.example
License # 5320417
Looking forward to the designs u come up with.
Thank you!
-Teresa
The designer (Brynn), that I would like to work with requested an extension to allow time to create a couple designs for this project.
Target Market(s)
Plumbing
Industry/Entity Type
Plumbing
Contact Information for Business Card
Listed above
Font styles to use
Look and feel

```html
<!DOCTYPE html>
<html lang="en">
<head>
<meta charset="utf-8">
<title>Mossbrook Pipeworks – Business Card</title>
<link href="https://fonts.googleapis.com/css2?family=Montserrat:wght@400;700&display=swap" rel="stylesheet">
<style>
  :root {
    --backdrop: #d3d7d9;
    --paper: #f2f2f1;
    --brand-blue: #0a4fb0;
    --ink-grey: #6b6d70;
    --white: #ffffff;
  }
  * { box-sizing: border-box; margin: 0; padding: 0; }
  html, body {
    width: 1200px; height: 1051px; overflow: hidden;
    background: var(--backdrop);
    font-family: "Montserrat", sans-serif;
  }
  .sheet {
    width: 1200px; height: 1051px;
    display: flex; flex-direction: column;
    align-items: center; justify-content: center; gap: 60px;
  }
  .card {
    width: 760px; height: 434px;
    border-radius: 4px;
    box-shadow: 0 10px 30px rgba(0,0,0,.18);
    position: relative;
  }
  /* Front side */
  .card--front {
    background: var(--paper);
    display: flex; align-items: center;
    border-bottom: 3px solid var(--brand-blue);
  }
  .front__brand {
    width: 44%; height: 100%;
    display: flex; align-items: center; justify-content: center; gap: 12px;
  }
  .brand-dot {
    width: 26px; height: 26px; border-radius: 50%;
    background: var(--brand-blue); flex: none;
  }
  .brand-name {
    color: var(--brand-blue);
    font-weight: 700; font-size: 24px; line-height: 1.15;
    text-transform: uppercase;
  }
  .front__divider {
    width: 2px; height: 260px; background: var(--brand-blue);
  }
  .front__details {
    padding-left: 48px;
    display: flex; flex-direction: column;
  }
  .person-name {
    color: var(--brand-blue); font-weight: 700; font-size: 28px;
    text-transform: uppercase; letter-spacing: .5px;
  }
  .license {
    color: var(--ink-grey); font-size: 18px; margin-top: 6px; margin-bottom: 34px;
  }
  .contact-list { list-style: none; display: flex; flex-direction: column; gap: 12px; }
  .contact-item {
    display: flex; align-items: center; gap: 12px;
    color: var(--ink-grey); font-size: 18px;
  }
  .contact-item svg { width: 18px; height: 18px; flex: none; fill: var(--brand-blue); }
  /* Back side */
  .card--back {
    background: var(--brand-blue);
    display: flex; align-items: center; justify-content: center; gap: 16px;
  }
  .card--back .brand-dot { background: var(--white); width: 34px; height: 34px; }
  .card--back .brand-name { color: var(--white); font-size: 34px; }
</style>
</head>
<body>
<main class="sheet">
  <section class="card card--front">
    <div class="front__brand">
      <span class="brand-dot"></span>
      <span class="brand-name">Mossbrook<br>Pipeworks</span>
    </div>
    <div class="front__divider"></div>
    <div class="front__details">
      <h1 class="person-name">Dario Whitlock</h1>
      <p class="license">License # 5320417</p>
      <ul class="contact-list">
        <li class="contact-item">
          <svg viewBox="0 0 24 24" aria-hidden="true"><path d="M6.6 10.8a15.1 15.1 0 0 0 6.6 6.6l2.2-2.2a1 1 0 0 1 1-.25 11.4 11.4 0 0 0 3.6.57 1 1 0 0 1 1 1V20a1 1 0 0 1-1 1A17 17 0 0 1 3 4a1 1 0 0 1 1-1h3.5a1 1 0 0 1 1 1c0 1.25.2 2.45.57 3.57a1 1 0 0 1-.25 1z"/></svg>
          (555) 208-7713
        </li>
        <li class="contact-item">
          <svg viewBox="0 0 24 24" aria-hidden="true"><path d="M2 5h20v2l-10 6L2 7z"/><path d="M2 9l10 6 10-6v10H2z"/></svg>
          Info@mossbrookpipeworks.example
        </li>
        <li class="contact-item">
          <svg viewBox="0 0 24 24" aria-hidden="true"><path d="M12 2a10 10 0 1 0 0 20 10 10 0 0 0 0-20zm6.9 6h-2.9a15.7 15.7 0 0 0-1.4-3.6A8 8 0 0 1 18.9 8zM12 4c.8 1.2 1.5 2.5 1.9 4h-3.8c.4-1.5 1.1-2.8 1.9-4zM4.3 14a8 8 0 0 1 0-4h3.4a16.5 16.5 0 0 0 0 4zm.8 2H8a15.7 15.7 0 0 0 1.4 3.6A8 8 0 0 1 5.1 16zM8 8H5.1a8 8 0 0 1 4.3-3.6A15.7 15.7 0 0 0 8 8zm4 12c-.8-1.2-1.5-2.5-1.9-4h3.8c-.4 1.5-1.1 2.8-1.9 4zm2.3-6H9.7a14.7 14.7 0 0 1 0-4h4.6a14.7 14.7 0 0 1 0 4zm.3 5.6A15.7 15.7 0 0 0 16 16h2.9a8 8 0 0 1-4.3 3.6zM16.3 14a16.5 16.5 0 0 0 0-4h3.4a8 8 0 0 1 0 4z"/></svg>
          www.mossbrookpipeworks.example
        </li>
      </ul>
    </div>
  </section>

  <section class="card card--back">
    <span class="brand-dot"></span>
    <span class="brand-name">Mossbrook<br>Pipeworks</span>
  </section>
</main>
</body>
</html>
```